Cruise Booking Website

Cruise search and booking website

This project is a redesign of a cruise booking website we did a few years ago.

The current website is located here: http://voyage.pixelmarsh.com/en/

It's not fully functional but gives you ad idea how miserable the old design was.

All the information about cruises, cruise lines, destinations, ports and shore excursions will be similar to http://www.sailorbay.com/
Actual search pages (form, results, single result, sailing and cabin selection, ship info, booking) will have EXACTLY the same info as sailorbay.com

We like the style of http://harborvoyagehub.com, it's quite modern, good spacing, not overloaded with information. So you can use it as an example of what we like, not what we want as a final result for us. Please, don't copy it. The result should not be possible to resemble the harborvoyagehub.com, because our site has to be unique. This is important!
If you submit a design that clearly reminds another cruise site it will be rejected!

Also the mockup provided is just to give you the basic structure and show what information has to be present on the page. It doesn't mean the layout has to be the same as a mockup. The layout is up to the designer.

I've updated the mockup to be more generic so it doesn't confuse you:
https://www.filecrate.net/s/k7q2mz9pw4tnb3x/Home%20page.png

When you're adding social sharing icons like chatterbox/peeplet you have to use chinese ones instead:
https://www.filecrate.net/s/h3rt8wyd6jcl0fe/chinese-social-icons.png
Originals: http://shrtlk.example/qRmT

We'll start with home page first and after it's approved inner pages can be designed.

I know the cost of the project doesn't look high, but the task is straight forward and doesn't require to be very original, it's better to follow existing design and layout patterns that proved to work well.
That's why I encourage you to choose a template to build the design on top of one of https://themequarry.net/ themes if it will save the design work, will be easier and faster for you. So it will be more like a customization than a new design from scratch.

Mockups, site map and logo files:
- https://www.filecrate.net/sh/50xb7vq1ndtpkez/RmwuHp8Zq3

Website tree:
- https://papers.quillnet.example/document/d/8vTrXk2MqLpZ4wNsB7yHcE1oUjFgD9aR_QbVtnWm/edit?usp=sharing
Updates

So far a lot of designs are just copying http://www.harborvoyagehub.com/ - we don't like it!

We like the style of harborvoyagehub.com, it's quite modern, good spacing, not overloaded with information. So you can use it as an example of what we like, not what we want as a final result for us. Please, don't copy it. The result should not be possible to resemble the harborvoyagehub.com, because our site has to be unique. This is important!

Target Market(s)

Chinese travellers

Industry/Entity Type

Build

Requirements
Must have
• * White, blue and red
* Large spacing, not too much information cramped into a small space like sailorbay.com or the current website
* More "hidden" info in popups, tabs and so on, so not to many things are visible at the same time
* Compatible with lumen framekit styling (for easier coding):
- http://lumenkit.example.io/framework/index.html
- http://skinvault.net/
* Feel free to propose to build the design on top of one of https://themequarry.net/ themes if it will save the design work, will be easier and faster for you

```html
<!DOCTYPE html>
<html lang="en">
<head>
<meta charset="utf-8">
<title>Bluewake Cruises – Search Results</title>
<link href="https://fonts.googleapis.com/css2?family=PT+Sans:wght@400;700&display=swap" rel="stylesheet">
<style>
:root{
  --blue:#1d5ea6;
  --blue-dark:#14508f;
  --blue-link:#1b63b5;
  --nav-top:#2a78c8;
  --nav-bot:#1557a0;
  --nav-active:#3b94e2;
  --orange:#f77a12;
  --orange-dark:#e2600a;
  --ink:#2a2a2a;
  --muted:#666;
  --line:#dfe4ea;
  --box:#f4f5f6;
  --footer:#2f6aa6;
  --footer-dark:#285f97;
}
*{box-sizing:border-box;margin:0;padding:0}
html,body{width:1086px;height:1200px;overflow:hidden}
body{
  font-family:"PT Sans",sans-serif;color:var(--ink);
  background:radial-gradient(ellipse 70% 60% at 50% 18%,#6ea6da 0%,#2f6fae 55%,#1b528d 100%);
  position:relative;
}
.page{position:absolute;left:163px;top:0;width:760px;height:1200px;background:#fff}
.abs{position:absolute}

/* header */
.brand{left:12px;top:30px;display:flex;align-items:center;gap:7px}
.brand-mark{width:36px;height:36px;border-radius:50%;background:var(--blue)}
.brand-name{font-size:26px;font-weight:700;color:var(--blue);letter-spacing:-.5px}
.account{left:556px;top:15px;font-size:10px;color:var(--blue-link)}
.account span{margin:0 8px;color:#555}
.social{left:654px;top:12px;display:flex;gap:4px}
.social i{display:block;width:20px;height:20px;border-radius:3px}
.call{left:412px;top:44px;display:flex;gap:8px;align-items:center}
.call svg{width:30px;height:30px}
.call-num{font-size:17.5px;font-weight:700;color:var(--blue);line-height:1}
.call-note{font-size:13px;color:#333;line-height:1.2}
.search{left:566px;top:59px;width:178px;height:20px;border:1px solid #c9c9c9;border-radius:2px;
  font-size:7px;color:#888;padding:6px 8px;box-shadow:inset 0 1px 2px rgba(0,0,0,.08)}
.search svg{position:absolute;right:5px;top:4px;width:11px;height:11px}

.nav{left:0;top:101px;width:760px;height:30px;display:flex;
  background:linear-gradient(var(--nav-top),var(--nav-bot))}
.nav a{display:flex;align-items:center;justify-content:center;font-size:9px;font-weight:700;
  color:#fff;text-decoration:none;border-right:1px solid rgba(0,0,0,.12)}
.nav a.active{background:var(--nav-active)}

/* sidebar search */
.finder{left:17px;top:150px;width:223px;height:315px;background:var(--blue);
  border:2px solid #1a5597;border-radius:2px;color:#d8e6f5}
.finder h2{position:absolute;left:18px;top:16px;font-size:20px;font-weight:400;color:#fff}
.finder .rule{position:absolute;left:0;right:0;top:42px;height:1px;background:rgba(255,255,255,.18)}
.lbl{position:absolute;font-size:10.5px;color:#d8e6f5}
.field{position:absolute;height:21px;background:linear-gradient(#f6f6f6,#dedede);border-radius:2px;
  font-size:8px;color:#333;padding:6px 8px}
.field::after{content:"";position:absolute;right:0;top:0;width:16px;height:100%;border-left:1px solid #bbb;
  background:linear-gradient(#f6f6f6,#e2e2e2)}
.field svg{position:absolute;right:4px;top:5px;width:8px;height:11px;z-index:1}
.check{position:absolute;left:18px;top:253px;font-size:8px;display:flex;gap:4px;align-items:center}
.check i{width:10px;height:10px;background:#dfe6ee;border-radius:1px}
.btn-search{position:absolute;left:18px;top:269px;width:190px;height:30px;border-radius:3px;
  background:linear-gradient(#fb9233,var(--orange-dark));color:#fff;font-size:13.5px;
  display:flex;align-items:center;justify-content:center;border:1px solid #fff}

/* newsletter */
.news{left:17px;top:486px;width:223px;height:269px;background:linear-gradient(#2b6fb5,var(--blue-dark));
  border-radius:2px;color:#fff}
.news-photo{position:absolute;left:10px;top:11px;width:203px;height:122px;background:#fff;padding:4px}
.news-photo div{width:100%;height:100%;background:linear-gradient(160deg,#4fb2d6,#3d7fa9 45%,#c9b49a)}
.news h3{position:absolute;left:18px;top:143px;font-size:12px}
.news p{position:absolute;left:18px;top:163px;font-size:7.5px}
.news-email{position:absolute;left:18px;top:185px;width:194px;height:21px;background:#fff;border-radius:2px;
  font-size:8px;color:#888;padding:5px 0 0 43px}
.btn-sub{position:absolute;left:18px;top:216px;width:80px;height:20px;background:#15427a;border-radius:2px;
  font-size:8.5px;display:flex;align-items:center;justify-content:center}
.contest{position:absolute;left:21px;top:242px;font-size:9px}

/* results */
.crumb{left:267px;top:150px;font-size:8.5px;color:var(--blue-link)}
.crumb span{margin:0 6px;color:#777}
.results-bar{left:262px;top:176px;width:481px;height:29px;background:linear-gradient(#fafafa,#ececec);
  border:1px solid var(--line)}
.results-bar b{position:absolute;left:12px;top:8px;font-size:11px;color:var(--blue)}
.results-bar small{font-size:6.5px;color:#555;font-weight:400;margin-left:3px}
.pager{display:flex;gap:4px}
.pager i{font-style:normal;min-width:15px;height:15px;padding:0 4px;border:1px solid #d2d2d2;border-radius:1px;
  background:#fff;font-size:6.5px;font-weight:700;display:flex;align-items:center;justify-content:center;color:#333}
.pager i.wide{min-width:30px}
.results-bar .pager{position:absolute;right:7px;top:6px}

.result{position:absolute;left:262px;width:481px;height:157px;border-bottom:1px solid var(--line)}
.thumb{position:absolute;left:0;top:0;width:167px;height:122px;border:1px solid #ddd;padding:4px;background:#fff}
.thumb div{width:100%;height:100%}
.sea-a{background:linear-gradient(#3f8fd1 0%,#8fc3ea 45%,#f3f5f7 60%,#1f5f98 85%)}
.sea-b{background:linear-gradient(#6f7880 0%,#b9c2c8 40%,#eef0f1 65%,#3d4a55 100%)}
.sea-c{background:linear-gradient(#8aa8c6 0%,#e8ecef 40%,#f6f6f6 60%,#35557a 100%)}
.sea-d{background:linear-gradient(#4b8cd0 0%,#a8cdee 40%,#f1f4f6 55%,#1e5a95 100%)}
.ribbon{position:absolute;left:4px;top:4px;width:60px;height:60px;overflow:hidden}
.ribbon span{position:absolute;left:-22px;top:14px;width:100px;transform:rotate(-45deg);background:var(--blue);
  color:#fff;font-size:7px;text-align:center;padding:2px 0}
.r-title{position:absolute;left:180px;top:0;font-size:11.5px;font-weight:700;color:var(--blue)}
.r-line{position:absolute;left:180px;top:19px;font-size:8.5px;color:#222}
.r-ports{position:absolute;left:180px;top:37px;font-size:8.5px;color:#222}
.r-ports a{color:var(--blue-link);text-decoration:none}
.r-ports span{margin:0 6px}
.prices{position:absolute;left:180px;top:60px;display:flex;gap:3px}
.price{width:72px;height:43px;border:1px solid var(--line);background:linear-gradient(#fff,var(--box));
  text-align:center;font-size:7.5px;line-height:11px;padding-top:4px;color:#555}
.price b{display:block;font-weight:400;color:var(--blue-link)}
.select{position:absolute;left:424px;top:114px;width:54px;height:16px;border-radius:2px;background:var(--orange);
  color:#fff;font-size:6.5px;display:flex;align-items:center;justify-content:center}
.select.primary{background:linear-gradient(#2c72bd,var(--blue-dark))}

.pager-bottom{left:510px;top:852px}

/* partners */
.partners-title{left:13px;top:884px;font-size:14px;font-weight:700;color:var(--blue)}
.arrows{left:712px;top:885px;display:flex;gap:3px}
.arrows i{width:15px;height:15px;background:#c9c9c9;display:flex;align-items:center;justify-content:center}
.partners{left:15px;top:913px;display:flex;gap:12px}
.partner{width:112px;height:56px;border:1px solid #d9d9d9;display:flex;align-items:center;justify-content:center}
.partner i{display:block;width:50px;height:14px;border-radius:7px}

/* footer */
.footer{left:0;top:989px;width:760px;height:173px;background:var(--footer);color:#fff}
.footer h4{position:absolute;font-size:12px;font-weight:700}
.footer ul{position:absolute;list-style:none;font-size:7.8px;line-height:17px}
.about-logo{position:absolute;left:314px;top:58px;width:76px;height:74px;background:#fff;display:flex;
  flex-direction:column;align-items:center;justify-content:center;gap:5px}
.about-logo i{width:30px;height:30px;border-radius:50%;background:var(--blue)}
.about-logo span{font-size:8px;font-weight:700;color:var(--blue)}
.about-text{position:absolute;left:406px;top:62px;width:90px;font-size:8.8px;line-height:13.5px}
.contact{position:absolute;left:547px;top:57px;font-size:9.5px;line-height:15px}
.contact p{display:flex;gap:5px;align-items:center;margin-top:5px}
.contact svg{width:11px;height:9px}
.legal{left:0;top:1162px;width:760px;height:38px;background:var(--footer-dark);color:#fff;font-size:7.5px;
  display:flex;align-items:center;justify-content:center}
</style>
</head>
<body>
<div class="page">

  <header>
    <div class="abs brand"><span class="brand-mark"></span><span class="brand-name">Bluewake Cruises</span></div>
    <div class="abs account">Sign in<span>|</span>Signup</div>
    <div class="abs social" aria-label="Social links">
      <i style="background:#e6302c"></i><i style="background:#29a7df"></i><i style="background:#f08a1c"></i><i style="background:#d9342b"></i>
    </div>
    <div class="abs call">
      <svg viewBox="0 0 30 30"><circle cx="15" cy="15" r="13.5" fill="none" stroke="#666" stroke-width="1.4"/><path d="M11 8c-2 1-2 4 0 8s5 7 8 7c1.5 0 2.5-1 2-2l-2-2-2 1c-1.5-.5-4-3.5-4.5-5l1-2-2-3z" fill="#555"/></svg>
      <div><div class="call-num">400 218 508</div><div class="call-note">Call Us Today!</div></div>
    </div>
    <div class="abs search">SEARCH :
      <svg viewBox="0 0 12 12"><circle cx="5" cy="5" r="3.6" fill="none" stroke="#aaa" stroke-width="1.3"/><path d="M7.7 7.7L11 11" stroke="#aaa" stroke-width="1.3"/></svg>
    </div>
    <nav class="abs nav">
      <a style="width:79px">HOME</a><a class="active" style="width:107px">DESTINATIONS</a><a style="width:101px">CRUISE LINES</a>
      <a style="width:96px">CRUISE INFO</a><a style="width:72px">DEALS</a><a style="width:119px">ONLINE BOOKING</a>
      <a style="width:99px">CONTACT US</a><a style="width:87px;border:0">BLOG</a>
    </nav>
  </header>

  <aside class="abs finder">
    <h2>Find Your Cruise</h2><div class="rule"></div>
    <div class="lbl" style="left:18px;top:53px">Destination</div>
    <div class="field" style="left:18px;top:68px;width:185px">Destination name<svg viewBox="0 0 8 11"><path d="M1 4L4 1 7 4zM1 7l3 3 3-3z" fill="#777"/></svg></div>
    <div class="lbl" style="left:18px;top:95px">Length</div>
    <div class="lbl" style="left:119px;top:95px">Month</div>
    <div class="field" style="left:18px;top:110px;width:84px">Length Area</div>
    <div class="field" style="left:119px;top:110px;width:84px"><svg viewBox="0 0 8 11"><path d="M1 4L4 1 7 4zM1 7l3 3 3-3z" fill="#777"/></svg></div>
    <div class="lbl" style="left:16px;top:139px">Cruise Lines</div>
    <div class="field" style="left:16px;top:153px;width:188px">Any Cruise line<svg viewBox="0 0 8 11"><path d="M1 4L4 1 7 4zM1 7l3 3 3-3z" fill="#777"/></svg></div>
    <div class="lbl" style="left:16px;top:184px;font-size:12px">Number of Travelers</div>
    <div class="lbl" style="left:18px;top:205px">Age 25+</div>
    <div class="lbl" style="left:119px;top:205px">Age 0 to 24</div>
    <div class="field" style="left:18px;top:221px;width:83px">5<svg viewBox="0 0 8 11"><path d="M1 4L4 1 7 4zM1 7l3 3 3-3z" fill="#777"/></svg></div>
    <div class="field" style="left:119px;top:221px;width:84px">0<svg viewBox="0 0 8 11"><path d="M1 4L4 1 7 4zM1 7l3 3 3-3z" fill="#777"/></svg></div>
    <div class="check"><i></i>Check for senior rates</div>
    <div class="btn-search">Search Cruises</div>
  </aside>

  <aside class="abs news">
    <div class="news-photo"><div role="img" aria-label="Senior couple relaxing in deck chairs by a pool"></div></div>
    <h3>Cruise Deals Newsletter</h3>
    <p>Subscribe to the best Cruise deals Now!</p>
    <div class="news-email">Email :</div>
    <div class="btn-sub">Subscribe</div>
    <div class="contest">Contest Rules</div>
  </aside>

  <div class="abs crumb">HOME<span>›</span>SEARCH</div>
  <div class="abs results-bar"><b>CRUISE RESULTS<small>76 FOUND</small></b>
    <div class="pager"><i class="wide">Prev</i><i>1</i><i>2</i><i>3</i><i>4</i><i>5</i><i>6</i><i>...</i><i>22</i><i class="wide">Next</i></div>
  </div>

  <article class="result" style="top:226px">
    <div class="thumb"><div class="sea-a" role="img" aria-label="White cruise ship at sea under blue sky"></div></div>
    <div class="ribbon"><span>NEW SHIP</span></div>
    <div class="r-title">3 DAYS BAHAMAS</div>
    <div class="r-line">NORDIC STAR CRUISE LINE. NORDIC SKY</div>
    <div class="r-ports"><a>Miami, Great ay, Nassau, Miami</a><span>|</span>4 departure dates : Sep 6, 13, 20, 27 2013</div>
    <div class="prices">
      <div class="price">Inside from<b>$174</b>$58 per day</div><div class="price">Ocean view from<b>$174</b>$58 per day</div>
      <div class="price">Inside from<b>$174</b>$58 per day</div><div class="price">Inside from<b>$174</b>$58 per day</div>
    </div>
    <div class="select primary">SELECT</div>
  </article>

  <article class="result" style="top:383px">
    <div class="thumb"><div class="sea-b" role="img" aria-label="Cruise ship docked beneath a harbour bridge"></div></div>
    <div class="r-title">3 DAYS BAHAMAS</div>
    <div class="r-line">NORDIC STAR CRUISE LINE. NORDIC SKY</div>
    <div class="r-ports"><a>Miami, Great ay, Nassau, Miami</a><span>|</span>4 departure dates : Sep 6, 13, 20, 27 2013</div>
    <div class="prices">
      <div class="price">Inside from<b>$174</b>$58 per day</div><div class="price">Ocean view from<b>$174</b>$58 per day</div>
      <div class="price">Inside from<b>$174</b>$58 per day</div><div class="price">Inside from<b>$174</b>$58 per day</div>
    </div>
    <div class="select">SELECT</div>
  </article>

  <article class="result" style="top:539px">
    <div class="thumb"><div class="sea-c" role="img" aria-label="Ferry-style cruise ship leaving port"></div></div>
    <div class="r-title">3 DAYS BAHAMAS</div>
    <div class="r-line">NORDIC STAR CRUISE LINE. NORDIC SKY</div>
    <div class="r-ports"><a>Miami, Great ay, Nassau, Miami</a><span>|</span>4 departure dates : Sep 6, 13, 20, 27 2013</div>
    <div class="prices">
      <div class="price">Inside from<b>$174</b>$58 per day</div><div class="price">Ocean view from<b>$174</b>$58 per day</div>
      <div class="price">Inside from<b>$174</b>$58 per day</div><div class="price">Inside from<b>$174</b>$58 per day</div>
    </div>
    <div class="select">SELECT</div>
  </article>

  <article class="result" style="top:696px">
    <div class="thumb"><div class="sea-d" role="img" aria-label="Cruise ship sailing on open blue ocean"></div></div>
    <div class="r-title">3 DAYS BAHAMAS</div>
    <div class="r-line">NORDIC STAR CRUISE LINE. NORDIC SKY</div>
    <div class="r-ports"><a>Miami, Great ay, Nassau, Miami</a><span>|</span>4 departure dates : Sep 6, 13, 20, 27 2013</div>
    <div class="prices">
      <div class="price">Inside from<b>$174</b>$58 per day</div><div class="price">Ocean view from<b>$174</b>$58 per day</div>
      <div class="price">Inside from<b>$174</b>$58 per day</div><div class="price">Inside from<b>$174</b>$58 per day</div>
    </div>
    <div class="select">SELECT</div>
  </article>

  <div class="abs pager pager-bottom"><i class="wide">Prev</i><i>1</i><i>2</i><i>3</i><i>4</i><i>5</i><i>6</i><i>...</i><i>22</i><i class="wide">Next</i></div>

  <div class="abs partners-title">OUR RELIABLE PARTNERS</div>
  <div class="abs arrows">
    <i><svg width="6" height="8" viewBox="0 0 6 8"><path d="M5 0L1 4l4 4" fill="none" stroke="#fff" stroke-width="1.5"/></svg></i>
    <i><svg width="6" height="8" viewBox="0 0 6 8"><path d="M1 0l4 4-4 4" fill="none" stroke="#fff" stroke-width="1.5"/></svg></i>
  </div>
  <div class="abs partners">
    <div class="partner"><i style="background:#c23a2a"></i></div>
    <div class="partner"><i style="background:#1d4f9c"></i></div>
    <div class="partner"><i style="background:#3d5a78"></i></div>
    <div class="partner"><i style="background:#f29a2e"></i></div>
    <div class="partner"><i style="background:#3aa4dd"></i></div>
    <div class="partner"><i style="background:#2b79c5"></i></div>
  </div>

  <footer class="abs footer">
    <h4 style="left:25px;top:28px">Useful Pages</h4>
    <ul style="left:25px;top:51px"><li>About Us</li><li>Contact us</li><li>Blog</li><li>FAQ</li><li>Terms of Service</li><li>Payment info</li><li>Reward Points</li></ul>
    <h4 style="left:172px;top:28px">Cruise Infov</h4>
    <ul style="left:173px;top:51px"><li>Cruise news</li><li>Visa</li><li>Honeymoon cruises</li><li>Firsttime on a Cruise</li></ul>
    <h4 style="left:314px;top:34px">About Bluewake</h4>
    <div class="about-logo"><i></i><span>Bluewake</span></div>
    <p class="about-text">We're the most advanced cruise booking providr in china.</p>
    <h4 style="left:547px;top:34px">Contact Us</h4>
    <div class="contact">
      Harbourline Studio,Pte Ltd<br>Tidewater Centre x118, Quay Road 7<br>Port Alden 20871
      <p><svg viewBox="0 0 11 9"><path d="M1 3c2-2 7-2 9 0v2H8V4H3v1H1zM3 5h5l1 3H2z" fill="#fff"/></svg>(404) 310-2286 - (404) 310-2287</p>
      <p style="margin-top:2px"><svg viewBox="0 0 11 9"><rect x="0.5" y="0.5" width="10" height="8" fill="#fff"/><path d="M1 1l4.5 4L10 1" fill="none" stroke="#2f6aa6"/></svg>hello@bluewakecruise.example</p>
    </div>
  </footer>
  <div class="abs legal">© 2013. Bluewake Cruises. All rights reserved.</div>
</div>
</body>
</html>
```